Commercial Auto Insurance Application and Commercial Property Insurance Application

Hi I need a fillable application for my business to send to potential clients for Commercial Auto Insurance and Commercial Property Insurance. I have attached an example application I currently use for another line of insurance.
Commercial Auto Insurance Application
On the first page I would need the following:
- Business Name: (fill in area for text)
- Effective Date: (fill in area for text)
- How do you structure your business? (Check box for “Sole Proprietor”, “Partnership”, “Corporation”, “LLC”)
- Contact Name: (fill in area for text) / Phone Number: (fill in area for text) / Contact Email (fill in area for text)
- Mailing address: (fill in area for text)
- Garaging location: (fill in area for text)
- Owner Name: (fill in area for text)
- Description of Operations: (fill in area for text)
- How long has the operation been in business? (fill in area for text)
- How many years of experience does your management have in the truck/transportation industry? (fill in area for text)
Coverages
Liability Combined Single Limit: ($1,000,000 (checkbox) / $500,000 (checkbox / $300,000 (checkbox) / Other: (fill in area for text)
Uninsured Motorist CSL: (fill in area for text) (checkbox for “Rejected”)
Medical Payments: (fill in area for text)
Physical Damage: (fill in area for text) (checkbox for Rejected)
Liability Deducible: ($500 checkbox, $1,000 checkbox, $2,500 checkbox, $5,000 checkbox)
Physical Damage Deductible: ($500 checkbox, $1,000 checkbox, $2,500 checkbox, $5,000 checkbox)
Driving radius: (fill in area for text)
How many years have you had your own continuous commercial auto insurance coverage for the current business name? (fill in area for text)
Do any of your vehicles travel across state lines? Yes (checkbox)/ No (checkbox)
If yes, please list all states in which vehicles operate: (fill in area for text)
What is the maximum radius traveled for your customer's business?
0-25 miles (checkbox)
26-50 miles (checkbox)
51-75 miles (checkbox)
76-100 miles (checkbox)
101-150 miles (checkbox)
151-200 miles (checkbox)
201-300 miles (checkbox)
300+ miles (checkbox)
Would you like physical damage coverage for this vehicle? (should be for each vehicle listed)
On the 2nd page of the application I would need the following:
I would need to have it where people can fill in the vehicle information such as VIN:, Year:, Make:, Model:, Type of Vehicle:, Trailers:, Value:
I would also need to have it where people can fill in the drivers with their driver info including Name:, DOB:, DL #:, DL State:, Class of License:, Married: Yes/No, Number of years driving similar vehicle:
Please make it where you can fill in 20 vehicle's information and 20 driver's info.
For the 2nd Application I would need one for Property Insurance
On the Commercial Property Application I would need the following:
- Building Address: (fill in area for text)
- Building Description: (fill in area for text)
- Building Amount: $(fill in area for text)
- Business Personal Property Amount: $ (fill in area for text) (checkbox for Not Needed)
- Building Sq Ft: (fill in area for text)
- Total Area Sq Ft: (fill in area for text)
- Building Construction Type: Wood Frame (checkbox), Steel (checkbox), Fire Resistive (checkbox), Non-Combustible (checkbox), Other (fill in area for text)
- # of stories: (fill in area for text)
- Year Built: (fill in area for text)
- Wiring improvement year: (fill in area for text)
- Roofing improvement year: (fill in area for text)
- Plumbing improvement year: (fill in area for text)
- Heating improvement year: (fill in area for text)
- What is to the right of the building and distance: (fill in area for text)
- What is to the left of the building and distance: (fill in area for text)
- What is in front of the building and distance: (fill in area for text)
- What is behind the building and distance: (fill in area for text)
- Burglar alarm installation and serviced by: (fill in area for text) None (checkbox)
- Does the premises have fire protection? Sprinkler system (checkbox), Fire detection (checkbox), Other: (fill in area for text) None (checkbox)

```html
<!DOCTYPE html>
<html lang="en">
<head>
<meta charset="utf-8">
<title>Commercial Auto &amp; Property Insurance Applications</title>
<link href="https://fonts.googleapis.com/css2?family=Poppins:wght@400;500;600;700;800&display=swap" rel="stylesheet">
<style>
:root{
  --navy:#253c7c;
  --green:#1f9a4a;
  --teal:#1f5f6f;
  --sky:#dce5ec;
  --row:#dde5ec;
  --line:#c9d3dc;
  --ink:#1e2a45;
  --bg:#ffffff;
}
*{box-sizing:border-box;margin:0;padding:0}
html,body{width:1200px;height:2325px;overflow:hidden;background:var(--bg);font-family:'Poppins',sans-serif;color:var(--ink)}
.canvas{position:relative;width:1200px;height:2325px}
.page{position:absolute;background:#fff;box-shadow:0 0 12px rgba(30,40,60,.18)}
.page--auto{left:40px;top:32px;width:546px;height:1122px}
.page--property{left:40px;top:1166px;width:546px;height:1125px}
.page--vehicles{left:614px;top:34px;width:545px;height:706px}
.page--drivers{left:614px;top:771px;width:545px;height:706px}

/* header */
.masthead{position:relative;height:168px;background:var(--sky);overflow:hidden}
.masthead__band{position:absolute;left:0;top:88px;width:100%;height:73px;background:linear-gradient(90deg,var(--navy) 0%,#24507a 45%,#1f7c5c 75%,var(--green) 100%)}
.masthead__stripe{position:absolute;left:0;top:161px;width:100%;height:7px;background:var(--green)}
.masthead__visual{position:absolute;left:290px;top:40px;width:256px;height:121px}
.masthead__visual--auto{background:linear-gradient(100deg,#267a57 0%,#2a8a4e 55%,#4a86c0 75%,#c94a4a 100%)}
.masthead__visual--city{background:linear-gradient(100deg,#267a57 0%,#2a8a4e 55%,#6f9fd0 78%,#27457a 100%)}
.brand{position:absolute;left:29px;top:30px;display:flex;align-items:center;gap:6px;color:var(--navy);font-weight:700;font-size:15px;line-height:1}
.brand__mark{width:9px;height:9px;background:var(--navy)}
.office{position:absolute;right:23px;top:20px;text-align:right;font-size:7.4px;line-height:12.2px;color:var(--ink);font-style:normal}
.masthead__title{position:absolute;left:29px;top:108px;color:#fff}
.masthead__kicker{font-size:11.5px;font-weight:400;line-height:1}
.masthead__main{font-size:28px;font-weight:800;line-height:1;letter-spacing:.3px;margin-top:1px}

/* sections */
.section{position:absolute;left:31px;width:484px}
.section__title{height:32px;background:linear-gradient(90deg,var(--navy) 0%,var(--teal) 50%,var(--green) 100%);color:#fff;font-weight:700;font-size:12.5px;display:flex;align-items:center;padding-left:10px}
.table{border-left:1px solid var(--line);border-right:1px solid var(--line);border-bottom:1px solid var(--line)}
.row{display:flex;height:26px;font-size:7px}
.row:nth-child(odd){background:var(--row)}
.row--head{font-weight:700;font-size:7.6px}
.field{width:191px;flex:none;padding:0 10px;display:flex;align-items:center;border-right:1px solid var(--line);line-height:1.45}
.field--small{font-size:6.2px}
.detail{flex:1;padding:0 8px;display:flex;flex-direction:column;justify-content:center;gap:5px}
.fill{display:flex;justify-content:space-between}
.fill--line{border-bottom:1px solid var(--line);padding-bottom:2px;width:272px}
.checks{display:flex;flex-wrap:wrap;gap:3px 6px;align-items:center}
.checks--tight{gap:4px 4px;font-size:6.1px}
.check{display:flex;align-items:center;gap:3px;white-space:nowrap}
.check::before{content:"";width:7px;height:7px;border:1px solid var(--ink);background:#fff;flex:none}
.or{margin-left:4px}

/* grids */
.grid-block{position:absolute;left:30px;width:485px}
.grid{width:485px;border-collapse:collapse;table-layout:fixed;font-size:7.4px}
.grid th{height:25px;font-weight:600;background:var(--row);border-left:1px solid var(--line);border-right:1px solid var(--line)}
.grid td{height:25.7px;text-align:center;border:1px solid var(--line);border-top:none;border-bottom:none}
.grid tbody tr:nth-child(even) td{background:var(--row)}
.grid tbody tr:last-child td{border-bottom:1px solid var(--line)}
.grid td .checks{justify-content:center;gap:4px;font-size:6px}
.grid--extra td{height:27px}
.grid--extra tr:nth-child(odd) td{background:var(--row)}
.grid--extra tr:nth-child(even) td{background:#fff}
.question{height:32px;background:linear-gradient(90deg,var(--navy) 0%,var(--teal) 50%,var(--green) 100%);color:#fff;font-size:7.2px;font-weight:500;display:flex;align-items:center;padding-left:11px;gap:10px}
.question .check::before{border-color:#fff;background:transparent}
.question .checks{font-size:6px;gap:4px}
</style>
</head>
<body>
<div class="canvas">

<section class="page page--auto">
  <header class="masthead">
    <div class="masthead__band"></div>
    <div class="masthead__visual masthead__visual--auto" role="img" aria-label="Illustration of green mountains with a photo of a red car under an umbrella"></div>
    <div class="masthead__stripe"></div>
    <div class="brand"><span class="brand__mark"></span>Ridgeline Insurance</div>
    <address class="office">Ridgeline Insurance Services<br>4820 Larkspur Ave Suite 310<br>Fairview Heights 90516<br>Tel: (555) 014-2236</address>
    <div class="masthead__title"><div class="masthead__kicker">COMMERCIAL AUTO INSURANCE</div><div class="masthead__main">APPLICATION</div></div>
  </header>

  <div class="section" style="top:194px">
    <div class="section__title">BUSIESS INFORMATION</div>
    <div class="table">
      <div class="row row--head"><div class="field">FIELD</div><div class="detail">DETAILS</div></div>
      <div class="row"><div class="field">Business Name:</div><div class="detail"><div class="fill"><span>Fill in area(</span><span>)</span></div></div></div>
      <div class="row"><div class="field">Effective Date:</div><div class="detail"><div class="fill"><span>Fill in area(</span><span>)</span></div></div></div>
      <div class="row"><div class="field">Business Structure:</div><div class="detail"><div class="checks"><span class="check">Sole Proprietor</span><span class="check">Partnership</span><span class="check">Corporation</span><span class="check">LLC</span></div></div></div>
      <div class="row"><div class="field">Contact Name:</div><div class="detail"><div class="fill"><span>Fill in area(</span><span>)</span></div></div></div>
      <div class="row"><div class="field">Phone Number:</div><div class="detail"><div class="fill"><span>Fill in area(</span><span>)</span></div></div></div>
      <div class="row"><div class="field">Contact Email:</div><div class="detail"><div class="fill"><span>Fill in area(</span><span>)</span></div></div></div>
      <div class="row"><div class="field">Mailing Address:</div><div class="detail"><div class="fill"><span>Fill in area(</span><span>)</span></div></div></div>
      <div class="row"><div class="field">Garaging Location:</div><div class="detail"><div class="fill"><span>Fill in area(</span><span>)</span></div></div></div>
      <div class="row"><div class="field">Owner Name:</div><div class="detail"><div class="fill"><span>Fill in area(</span><span>)</span></div></div></div>
      <div class="row"><div class="field">Description of Operations:</div><div class="detail"><div class="fill"><span>Fill in area(</span><span>)</span></div></div></div>
      <div class="row"><div class="field">Years in Business:</div><div class="detail"><div class="fill"><span>Fill in area(</span><span>)</span></div></div></div>
      <div class="row"><div class="field">Management Experience in Trucking Industry:</div><div class="detail"><div class="fill"><span>Fill in area(</span><span>)</span></div></div></div>
    </div>
  </div>

  <div class="section" style="top:584px">
    <div class="section__title">COVERAGES</div>
    <div class="table">
      <div class="row row--head" style="height:25px"><div class="field">COVERAGE TYPE</div><div class="detail">DETAILS</div></div>
      <div class="row" style="height:39px"><div class="field">Liability Combined Single Limit:</div><div class="detail"><div class="checks"><span class="check">$1,000,000</span><span class="check">$500,000</span><span class="check">$300,000</span></div><div class="fill--line"><span class="check">Other</span></div></div></div>
      <div class="row" style="height:44px"><div class="field">Uninsured Motorist CSL:</div><div class="detail"><div class="checks"><span class="check">Rejected</span><span class="or">“OR”</span></div><div class="fill--line">Fill in area</div></div></div>
      <div class="row" style="height:28px"><div class="field">Medical Payments:</div><div class="detail"><div class="fill"><span>Fill in area(</span><span>)</span></div></div></div>
      <div class="row" style="height:45px"><div class="field">Physical Damage:</div><div class="detail"><div class="checks"><span class="check">Rejected</span><span class="or">“OR”</span></div><div class="fill--line">Fill in area</div></div></div>
      <div class="row" style="height:29px"><div class="field">Liability Deductible:</div><div class="detail"><div class="checks"><span class="check">$500</span><span class="check">$1000</span><span class="check">$2500</span><span class="check">$5000</span></div></div></div>
      <div class="row" style="height:27px"><div class="field">Physical Damage Deductible:</div><div class="detail"><div class="checks"><span class="check">$500</span><span class="check">$1000</span><span class="check">$2500</span><span class="check">$5000</span></div></div></div>
    </div>
  </div>

  <div class="section" style="top:872px">
    <div class="section__title">OPERATIONAL DETAILS</div>
    <div class="table">
      <div class="row row--head" style="height:25px"><div class="field">FIELD</div><div class="detail">DETAILS</div></div>
      <div class="row" style="height:29px"><div class="field">Driving Radius:</div><div class="detail"><div class="fill"><span>Fill in area(</span><span>)</span></div></div></div>
      <div class="row" style="height:48px"><div class="field field--small">How many years have you had your own continuous commercial auto insurance coverage for the current business name?</div><div class="detail"><div class="fill"><span>Fill in area(</span><span>)</span></div></div></div>
      <div class="row" style="height:25px"><div class="field">Driving Radius:</div><div class="detail"><div class="checks"><span class="check">Yes</span><span class="check">No</span></div></div></div>
      <div class="row" style="height:26px"><div class="field field--small">If yes, please list all states in which vehicles operate:</div><div class="detail"><div class="fill"><span>Fill in area(</span><span>)</span></div></div></div>
      <div class="row" style="height:40px"><div class="field field--small">What is the maximum radius traveled for your customer's business?</div><div class="detail"><div class="checks checks--tight"><span class="check">0-25 miles</span><span class="check">26-50 miles</span><span class="check">51-75 miles</span><span class="check">76-100 miles</span><span class="check">101-150 miles</span><span class="check">151-200 miles</span><span class="check">201-300 miles</span><span class="check">300+ miles</span></div></div></div>
    </div>
  </div>
</section>

<section class="page page--property">
  <header class="masthead">
    <div class="masthead__band"></div>
    <div class="masthead__visual masthead__visual--city" role="img" aria-label="Illustration of green mountains with a photo of glass office towers"></div>
    <div class="masthead__stripe"></div>
    <div class="brand"><span class="brand__mark"></span>Ridgeline Insurance</div>
    <address class="office">Ridgeline Insurance Services<br>4820 Larkspur Ave Suite 310<br>Fairview Heights 90516<br>Tel: (555) 014-2236</address>
    <div class="masthead__title"><div class="masthead__kicker">Commercial Property Insurance</div><div class="masthead__main">APPLICATION</div></div>
  </header>

  <div class="section" style="top:189px">
    <div class="section__title">BUSINESS INFORMATION</div>
    <div class="table">
      <div class="row row--head"><div class="field">FIELD</div><div class="detail">DETAILS</div></div>
      <div class="row"><div class="field">Business Name:</div><div class="detail"><div class="fill"><span>Fill in area(</span><span>)</span></div></div></div>
      <div class="row"><div class="field">Building Address:</div><div class="detail"><div class="fill"><span>Fill in area(</span><span>)</span></div></div></div>
      <div class="row"><div class="field">Building Description:</div><div class="detail"><div class="fill"><span>Fill in area(</span><span>)</span></div></div></div>
      <div class="row"><div class="field">Building Amount:</div><div class="detail"><div class="fill"><span>Fill in area(</span><span>)</span></div></div></div>
      <div class="row" style="height:56px"><div class="field">Business Personal Property Amount:</div><div class="detail"><div class="checks"><span class="check">Not Needed</span><span class="or">“OR”</span></div><div class="fill--line">Fill in area</div></div></div>
      <div class="row"><div class="field">Building Sq Ft:</div><div class="detail"><div class="fill"><span>Fill in area(</span><span>)</span></div></div></div>
      <div class="row" style="height:27px"><div class="field">Total Area Sq Ft:</div><div class="detail"><div class="fill"><span>Fill in area(</span><span>)</span></div></div></div>
    </div>
  </div>

  <div class="section" style="top:477px">
    <div class="section__title">BUILDING DETAILS</div>
    <div class="table">
      <div class="row row--head" style="height:25px"><div class="field">FIELD</div><div class="detail">DETAILS</div></div>
      <div class="row" style="height:53px"><div class="field">Building Construction Type:</div><div class="detail"><div class="checks checks--tight"><span class="check">Wood Frame</span><span class="check">Steel</span><span class="check">Fire Resistive</span><span class="check">Non-Combustible</span><span class="check">101-150 miles</span></div><div class="fill--line" style="font-size:6.1px"><span class="check">Other</span></div></div></div>
      <div class="row"><div class="field"># of Stories:</div><div class="detail"><div class="fill"><span>Fill in area(</span><span>)</span></div></div></div>
      <div class="row"><div class="field">Year Built:</div><div class="detail"><div class="fill"><span>Fill in area(</span><span>)</span></div></div></div>
      <div class="row"><div class="field">Wiring Improvement Year:</div><div class="detail"><div class="fill"><span>Fill in area(</span><span>)</span></div></div></div>
      <div class="row"><div class="field">Roofing Improvement Year:</div><div class="detail"><div class="fill"><span>Fill in area(</span><span>)</span></div></div></div>
      <div class="row"><div class="field">Plumbing Improvement Year:</div><div class="detail"><div class="fill"><span>Fill in area(</span><span>)</span></div></div></div>
      <div class="row"><div class="field">Heating Improvement Year:</div><div class="detail"><div class="fill"><span>Fill in area(</span><span>)</span></div></div></div>
    </div>
  </div>

  <div class="section" style="top:758px">
    <div class="section__title">SURROUNDING AREAS</div>
    <div class="table">
      <div class="row row--head" style="height:25px"><div class="field">FIELD</div><div class="detail">DETAILS</div></div>
      <div class="row" style="height:27px"><div class="field field--small">What is to the right of the building and distance:</div><div class="detail"><div class="fill"><span>Fill in area(</span><span>)</span></div></div></div>
      <div class="row" style="height:27px"><div class="field field--small">What is to the left of the building and distance:</div><div class="detail"><div class="fill"><span>Fill in area(</span><span>)</span></div></div></div>
      <div class="row" style="height:26px"><div class="field field--small">What is in front of the building and distance:</div><div class="detail"><div class="fill"><span>Fill in area(</span><span>)</span></div></div></div>
      <div class="row" style="height:26px"><div class="field field--small">What is behind the building and distance:</div><div class="detail"><div class="fill"><span>Fill in area(</span><span>)</span></div></div></div>
    </div>
  </div>

  <div class="section" style="top:937px">
    <div class="section__title">SECURITY &amp; FIRE PROTECTION</div>
    <div class="table">
      <div class="row row--head" style="height:25px"><div class="field">FIELD</div><div class="detail">DETAILS</div></div>
      <div class="row" style="height:54px"><div class="field field--small">Burglar alarm installation and serviced by:</div><div class="detail"><div class="checks"><span class="check">None</span><span class="or">“OR”</span></div><div class="fill--line">Fill in area</div></div></div>
      <div class="row" style="height:45px"><div class="field">Fire Protection:</div><div class="detail"><div class="checks"><span class="check">Sprinkler System</span><span class="check">Fire Detection</span><span class="check">None</span></div><div class="fill--line"><span class="check">Other</span></div></div></div>
    </div>
  </div>
</section>

<section class="page page--vehicles">
  <div class="grid-block" style="top:20px">
    <div class="section__title">VEHICLE INFORMATION</div>
    <table class="grid">
      <thead><tr><th>Vin</th><th>Year</th><th>Make</th><th>Model</th><th>Vehicle Type</th><th>Trailers</th><th>Value</th></tr></thead>
      <tbody>
        <tr><td>--</td><td>--</td><td>--</td><td>--</td><td>--</td><td>--</td><td>--</td></tr>
        <tr><td></td><td></td><td></td><td></td><td></td><td></td><td></td></tr>
        <tr><td></td><td></td><td></td><td></td><td></td><td></td><td></td></tr>
        <tr><td></td><td></td><td></td><td></td><td></td><td></td><td></td></tr>
        <tr><td></td><td></td><td></td><td></td><td></td><td></td><td></td></tr>
        <tr><td></td><td></td><td></td><td></td><td></td><td></td><td></td></tr>
        <tr><td></td><td></td><td></td><td></td><td></td><td></td><td></td></tr>
        <tr><td></td><td></td><td></td><td></td><td></td><td></td><td></td></tr>
        <tr><td></td><td></td><td></td><td></td><td></td><td></td><td></td></tr>
        <tr><td></td><td></td><td></td><td></td><td></td><td></td><td></td></tr>
        <tr><td></td><td></td><td></td><td></td><td></td><td></td><td></td></tr>
        <tr><td></td><td></td><td></td><td></td><td></td><td></td><td></td></tr>
        <tr><td></td><td></td><td></td><td></td><td></td><td></td><td></td></tr>
        <tr><td></td><td></td><td></td><td></td><td></td><td></td><td></td></tr>
        <tr><td></td><td></td><td></td><td></td><td></td><td></td><td></td></tr>
        <tr><td></td><td></td><td></td><td></td><td></td><td></td><td></td></tr>
        <tr><td></td><td></td><td></td><td></td><td></td><td></td><td></td></tr>
        <tr><td></td><td></td><td></td><td></td><td></td><td></td><td></td></tr>
        <tr><td></td><td></td><td></td><td></td><td></td><td></td><td></td></tr>
        <tr><td></td><td></td><td></td><td></td><td></td><td></td><td></td></tr>
      </tbody>
    </table>
    <div class="question" style="margin-top:8px">Would you like physical damage coverage for this vehicle? If Yes Write Down Their Names in each cell: <span class="checks"><span class="check">Yes</span><span class="check">No</span></span></div>
    <table class="grid grid--extra">
      <tr><td>Sedan</td><td>--</td><td>--</td><td>--</td><td>--</td><td>--</td><td>--</td></tr>
      <tr><td>--</td><td>--</td><td>--</td><td>--</td><td>--</td><td>--</td><td>--</td></tr>
    </table>
  </div>
</section>

<section class="page page--drivers">
  <div class="grid-block" style="top:20px">
    <div class="section__title">DRIVER INFORMATION</div>
    <table class="grid">
      <thead><tr><th>Name</th><th>DOB</th><th>DL</th><th>DL State</th><th>License Class</th><th>Married</th><th style="font-size:6.4px">Experience (Years)</th></tr></thead>
      <tbody>
        <tr><td>--</td><td>--</td><td>--</td><td>--</td><td>--</td><td><span class="checks"><span class="check">Yes</span><span class="check">No</span></span></td><td>--</td></tr>
        <tr><td></td><td></td><td></td><td></td><td></td><td><span class="checks"><span class="check">Yes</span><span class="check">No</span></span></td><td></td></tr>
        <tr><td></td><td></td><td></td><td></td><td></td><td><span class="checks"><span class="check">Yes</span><span class="check">No</span></span></td><td></td></tr>
        <tr><td></td><td></td><td></td><td></td><td></td><td><span class="checks"><span class="check">Yes</span><span class="check">No</span></span></td><td></td></tr>
        <tr><td></td><td></td><td></td><td></td><td></td><td><span class="checks"><span class="check">Yes</span><span class="check">No</span></span></td><td></td></tr>
        <tr><td></td><td></td><td></td><td></td><td></td><td><span class="checks"><span class="check">Yes</span><span class="check">No</span></span></td><td></td></tr>
        <tr><td></td><td></td><td></td><td></td><td></td><td><span class="checks"><span class="check">Yes</span><span class="check">No</span></span></td><td></td></tr>
        <tr><td></td><td></td><td></td><td></td><td></td><td><span class="checks"><span class="check">Yes</span><span class="check">No</span></span></td><td></td></tr>
        <tr><td></td><td></td><td></td><td></td><td></td><td><span class="checks"><span class="check">Yes</span><span class="check">No</span></span></td><td></td></tr>
        <tr><td></td><td></td><td></td><td></td><td></td><td><span class="checks"><span class="check">Yes</span><span class="check">No</span></span></td><td></td></tr>
        <tr><td></td><td></td><td></td><td></td><td></td><td><span class="checks"><span class="check">Yes</span><span class="check">No</span></span></td><td></td></tr>
        <tr><td></td><td></td><td></td><td></td><td></td><td><span class="checks"><span class="check">Yes</span><span class="check">No</span></span></td><td></td></tr>
        <tr><td></td><td></td><td></td><td></td><td></td><td><span class="checks"><span class="check">Yes</span><span class="check">No</span></span></td><td></td></tr>
        <tr><td></td><td></td><td></td><td></td><td></td><td><span class="checks"><span class="check">Yes</span><span class="check">No</span></span></td><td></td></tr>
        <tr><td></td><td></td><td></td><td></td><td></td><td><span class="checks"><span class="check">Yes</span><span class="check">No</span></span></td><td></td></tr>
        <tr><td></td><td></td><td></td><td></td><td></td><td><span class="checks"><span class="check">Yes</span><span class="check">No</span></span></td><td></td></tr>
        <tr><td></td><td></td><td></td><td></td><td></td><td><span class="checks"><span class="check">Yes</span><span class="check">No</span></span></td><td></td></tr>
        <tr><td></td><td></td><td></td><td></td><td></td><td><span class="checks"><span class="check">Yes</span><span class="check">No</span></span></td><td></td></tr>
        <tr><td></td><td></td><td></td><td></td><td></td><td><span class="checks"><span class="check">Yes</span><span class="check">No</span></span></td><td></td></tr>
        <tr><td></td><td></td><td></td><td></td><td></td><td><span class="checks"><span class="check">Yes</span><span class="check">No</span></span></td><td></td></tr>
      </tbody>
    </table>
  </div>
</section>

</div>
</body>
</html>
```